Buch-/E-Book-Cover für: Marlene Kuhfeld: Krähenmorgen. Notizen vom Flurende
Loralies Einfühlungsvermögen in das Projekt, ihre Nachfragen an der richtigen Stelle und ihre frischen Ideen haben zu einem ebook-Cover geführt, mit dem ich sehr zufrieden bin. Die Kommunikation war sehr angenehm und professionell. Danke!
Zielgruppe
E-Book: Satirische Kurzgeschichten rund um Schule und Bildung.
Zielgruppe: Leute mit Humor und Interesse an einem Einblick ins Klassenzimmer einer jungen Berliner Lehrerin. Schüler, Eltern, Lehrer, Referendare...
Aufgabenstellung
Möglichst keine Comics mit Sprechblasen, eher stilvoll, intellektuell, trotzdem frisch, jung und modern.
Helle Farben, gerne Andeutungen der Themen Schule, Bildung, Unterricht.
Die Kurzgeschichten meines E-Books sind schnelle Momentaufnahmen, sie könnten auch als Blog erscheinen statt als Buch, evtl. lässt sich dies auch im Design widerspiegeln (?).

```html
<!DOCTYPE html>
<html lang="de">
<head>
<meta charset="utf-8">
<title>Marlene Kuhfeld – Krähenmorgen. Notizen vom Flurende</title>
<link rel="stylesheet" href="https://fonts.googleapis.com/css2?family=IM+Fell+Double+Pica&family=Parisienne&family=Cormorant+Garamond:wght@600&display=swap">
<style>
  :root {
    --board-dark: #3c3d3f;
    --board-mid: #55575a;
    --board-light: #6a6c6f;
    --author-red: #f0242f;
    --chalk-white: #ffffff;
    --ledge-wood: #e2ac73;
    --ledge-shadow: #c58d57;
    --tablet-frame: #1b1c1e;
    --tablet-edge: #8a8c90;
    --screen-green: #1f7a3e;
    --screen-green-dark: #14512a;
    --apple-red: #c8261b;
    --apple-gold: #e0a23a;
  }
  * { margin: 0; padding: 0; box-sizing: border-box; }
  html, body { width: 800px; height: 1200px; overflow: hidden; }
  .cover {
    position: relative;
    width: 800px;
    height: 1200px;
    overflow: hidden;
  }
  .chalkboard {
    position: absolute;
    inset: 0 0 57px 0;
    background:
      radial-gradient(ellipse at 30% 30%, var(--board-light) 0%, transparent 55%),
      radial-gradient(ellipse at 75% 70%, var(--board-mid) 0%, transparent 60%),
      linear-gradient(180deg, var(--board-mid), var(--board-dark));
  }
  .ledge {
    position: absolute;
    left: 0; right: 0; bottom: 0;
    height: 57px;
    background: linear-gradient(180deg, var(--ledge-wood) 0%, var(--ledge-wood) 60%, var(--ledge-shadow) 100%);
    border-top: 2px solid #f2c48f;
  }
  .author {
    position: absolute;
    top: 104px;
    left: 0; right: 0;
    text-align: center;
    font-family: "IM Fell Double Pica", serif;
    font-size: 76px;
    line-height: 1;
    letter-spacing: -1px;
    text-transform: uppercase;
    color: var(--author-red);
  }
  .title {
    position: absolute;
    top: 250px;
    left: 0; right: 0;
    text-align: center;
    font-family: "Parisienne", cursive;
    font-size: 168px;
    line-height: 192px;
    color: var(--chalk-white);
  }
  .title span { display: block; }
  .tablet {
    position: absolute;
    left: 239px;
    top: 696px;
    width: 318px;
    height: 447px;
    background: var(--tablet-frame);
    border: 2px solid var(--tablet-edge);
    border-radius: 14px;
  }
  .screen {
    position: absolute;
    left: 19px;
    top: 25px;
    width: 276px;
    height: 388px;
    overflow: hidden;
    background:
      radial-gradient(circle at 50% 66%, var(--apple-gold) 0%, var(--apple-red) 22%, transparent 24%),
      linear-gradient(180deg, var(--screen-green) 0%, var(--screen-green-dark) 100%);
  }
  .subtitle {
    position: absolute;
    left: 0; right: 0;
    top: 14px;
    text-align: center;
    font-family: "Cormorant Garamond", serif;
    font-weight: 600;
    font-size: 66px;
    line-height: 102px;
    color: var(--chalk-white);
    transform: scaleX(0.82);
  }
  .subtitle span { display: block; }
</style>
</head>
<body>
  <main class="cover">
    <div class="chalkboard" role="img" aria-label="Grau abgewischte Schultafel mit Kreidespuren"></div>
    <div class="ledge" role="img" aria-label="Holzleiste der Tafel mit einem Stück Kreide"></div>

    <p class="author">Marlene Kuhfeld</p>
    <h1 class="title"><span>Krähen</span><span>morgen.</span></h1>

    <div class="tablet">
      <div class="screen" role="img" aria-label="Roter Apfel auf einem Buchstapel vor grüner Tafel">
        <h2 class="subtitle"><span>Notizen</span><span>vom</span><span>Flurende</span></h2>
      </div>
    </div>
  </main>
</body>
</html>
```